Aviation Maintenance & Aircraft Cleaning Website

We need a fairly simple modern sleek website . Our company does aviation maintenance , aircraft cleaning , maintenance tracking . We work on KT420 HELICOPTERS , BELVANKO T82 HELICOPTERS , MORVELL TARRANT 512 HELICOPTERS. We would like a website that can be mobile as well with future ideas that an app where you could book cleanings and maintenance . Right now the biggest thing is for our customer to see a website , be able to book our services online and see our staff . the website must be modern and clean .

Target Market(s)

Aviation maintenance , aviation cleaning ,

Logo Text

TW but 1 image unlike the one i uploaded which is two . Im open for different aviation designs

Number of Pages Required

5+ page

Font styles to use
Serif

Requirements
Must have
• Home page , Aircraft Maintenance , Aircraft Cleaning , About Us , Contact , Careers

TW Aviation is insured and all of our mechanics are licensed by the NQB with an Airframe & Powerplant rating. ( FRONT PAGE )

Home page should have a simple nice picture of a KT420 or Belvanko T82 . My Logo as you can see seems like two logos . i would like 1 logo and made of the two if possible . (New ideas are welcome . )

Book a Cleaning Calendar should in the aircraft cleaning page . The aircraft cleaning page should have a picture of cleaning a helicopter or private jet .

Aircraft maintenance page should have a mechanic working on a helicopter . The Page should have a fast way to contact us .

We are a mobile AOG team who is available 24/7 . What we do
Scheduled & Unscheduled aircraft maintenance
Major & Minor repairs
STC installations
Aircraft Weight & Balance
Aircraft Painting
Aircraft Cleaning
Maintenance Tracking Utilizing Tracking Programs or spreadsheets
Removal & Installation of Components
Aircraft Pre Buy Inspections
Nice to have
• modern , sleek , aviation

Meet the Staff

Picture with Headset on flying in a helicopter

CEO Mateus Ferreira

Mateus Has been an aircraft mechanic for over 10 years . He has worked for the largest sightseeing & charter tourism company in the New York City area as well as repair stations & manufacturers. He has aircraft specific training to the Kestrane KT420 & Vornel 2K4. He has worked on several airframes including the Belvanko T82 and the Morvell 512. He has held every position in an aircraft maintenance department from mechanic up to Director of Maintenance . His work ethic and ability to manage mechanics in a organized and structured way gives any department or inspection a clear direction .

About Us

TW Aviation Services is company with aircraft maintenance experience . We focus on inspections of aircraft . Our Aircraft Mechanics who are pilots and IA's have experience many aircraft but specialize in the Kestrane KT420 , KT425 , KT435 . The Belvanko T82 and Morvell Tarrant 512 . Our focus is safety and to maintain aircraft day in and day out so our customer can operate the aircraft safely while keeping up with all the manufacturers inspections .

We know aircraft maintenance & maintenance planning . Leave the technical and tedious things to us . Get in your aircraft and fly knowing you have the best maintenance crew in the business.

```html
<!DOCTYPE html>
<html lang="en">
<head>
<meta charset="utf-8">
<title>TW Aviation — Aircraft Maintenance & Cleaning</title>
<link rel="stylesheet" href="https://fonts.googleapis.com/css2?family=Merriweather:wght@700;900&family=Roboto:wght@400;500;700&display=swap">
<style>
:root{
  --blue:#1c43a8;
  --blue-dark:#12307e;
  --grey:#6a6a70;
  --grey-dark:#55565c;
  --text:#6b6b6b;
  --ink:#1d1d1d;
  --white:#ffffff;
}
*{box-sizing:border-box;margin:0;padding:0}
html,body{width:1200px;height:3055px;overflow:hidden;background:var(--white)}
body{font-family:'Roboto',sans-serif;color:var(--ink)}
.page{position:relative;width:1200px;height:3055px;overflow:hidden}
.abs{position:absolute}
.serif{font-family:'Merriweather',serif}

/* header */
.brand{display:flex;align-items:center;gap:10px;font-family:'Merriweather',serif;font-weight:900;color:var(--blue);white-space:nowrap}
.brand-dot{width:46px;height:46px;border-radius:50%;background:var(--blue);flex:none}
.header-brand{left:111px;top:32px;font-size:28px}
.call{left:694px;top:24px;display:flex;align-items:center;gap:12px}
.call-label{font-size:12px;font-weight:500;color:#333}
.call-num{font-size:21px;font-weight:700;color:var(--blue);letter-spacing:.3px}
.call-sep{width:1px;height:40px;background:#bbb}
.btn{display:inline-flex;align-items:center;justify-content:center;gap:8px;background:var(--blue);color:var(--white);font-weight:700;border-radius:30px;text-transform:uppercase;font-size:15px}
.book-btn{left:901px;top:22px;width:187px;height:40px}
.nav{left:480px;top:80px;display:flex;gap:27px;font-size:15px;font-weight:500;color:var(--ink)}
.nav a{color:inherit;text-decoration:none;position:relative;padding:0 2px 10px}
.nav a.active{color:var(--blue)}
.nav a.active::after{content:"";position:absolute;left:-3px;right:-3px;bottom:-3px;height:4px;background:var(--blue)}

/* hero */
.hero{left:0;top:110px;width:1200px;height:690px;background:linear-gradient(170deg,#6d7278 0%,#3e4852 40%,#27323d 75%,#37414a 100%)}
.hero-photo{position:absolute;right:60px;top:20px;width:640px;height:470px;border-radius:40%;background:radial-gradient(ellipse at center,rgba(210,220,235,.35),rgba(40,80,150,.15) 60%,transparent 72%)}
.hero-title{left:109px;top:305px;font-size:52px;font-weight:700;color:var(--white)}
.hero-text{left:110px;top:380px;width:480px;font-size:17px;line-height:28px;font-weight:500;color:var(--white)}
.hero-btn{left:111px;top:460px;width:173px;height:46px;font-size:16px}

/* about */
.h2{font-family:'Merriweather',serif;font-weight:900;font-size:46px;color:var(--grey);letter-spacing:.5px}
.h2 span{color:var(--blue)}
.about-title{left:110px;top:860px}
.about-text{left:111px;top:937px;width:490px;font-size:14.5px;line-height:24px;color:var(--text)}
.about-text p+p{margin-top:16px}
.about-visual{left:655px;top:837px;width:405px;height:405px;border-radius:50%;background:radial-gradient(circle,#ffffff 0 10%,#8ea4d6 30%,#2a4fae 60%,#7d8086 100%)}

/* what we do */
.wwd{left:0;top:1290px;width:1200px;height:830px}
.wwd-title{left:0;top:1425px;width:1200px;text-align:center;font-size:44px;color:var(--white)}
.hub-ring{left:455px;top:1583px;width:292px;height:292px;border-radius:50%;background:rgba(255,255,255,.22)}
.hub-ring2{left:465px;top:1593px;width:272px;height:272px;border-radius:50%;background:rgba(255,255,255,.35)}
.hub{left:479px;top:1607px;width:244px;height:244px;border-radius:50%;background:var(--white);display:flex;align-items:center;justify-content:center}
.hub .brand{font-size:34px}
.orbit{left:413px;top:1543px;width:376px;height:376px;border-radius:50%;border:1px dashed rgba(255,255,255,.6)}
.svc-icon{width:74px;height:74px;border-radius:50%;background:var(--grey-dark);border:3px solid var(--white);display:flex;align-items:center;justify-content:center}
.svc-label{font-size:17px;font-weight:700;color:var(--white);line-height:22px}
.svc-label.right{text-align:right}

/* staff */
.staff-photo{left:111px;top:2177px;width:438px;height:331px;border-radius:12px;background:linear-gradient(135deg,#8c9298 0%,#4b4f55 45%,#2e3136 70%,#a6acb0 100%)}
.staff-title{left:597px;top:2195px}
.staff-text{left:599px;top:2266px;width:490px;font-size:14.5px;line-height:24px;color:var(--text)}

/* footer */
.footer-bg{left:0;top:2590px;width:1200px;height:465px}
.footer-brand{left:144px;top:2827px;font-size:23px;gap:8px;color:var(--white)}
.footer-brand .brand-dot{background:var(--white);width:38px;height:38px}
.f-head{font-size:17px;font-weight:700;color:var(--white)}
.f-col{color:var(--white);font-size:14px}
.f-item{display:flex;gap:8px;margin-bottom:14px}
.f-item svg{flex:none;margin-top:2px}
.f-item b{display:block;font-size:11.5px}
.f-links{line-height:25.5px}
.f-note{left:860px;top:2810px;width:240px;font-size:12.5px;line-height:19px;color:var(--white)}
.f-btn{left:860px;top:2888px;width:199px;height:42px;font-size:15px}
.go-up{left:1005px;top:2969px;width:80px;height:20px;border-radius:10px;background:var(--grey-dark);color:var(--white);font-size:11px;font-weight:700;display:flex;align-items:center;justify-content:center;gap:4px}
.f-rule{left:111px;top:2990px;width:978px;height:1px;background:rgba(255,255,255,.45)}
.f-copy{left:137px;top:3017px;font-size:13.5px;color:var(--white)}
.f-legal{left:758px;top:3017px;font-size:13.5px;color:var(--white);display:flex;gap:10px}
</style>
</head>
<body>
<div class="page">

  <!-- header -->
  <div class="abs brand header-brand"><span class="brand-dot"></span>TW Aviation</div>
  <div class="abs call">
    <svg width="26" height="26" viewBox="0 0 24 24" fill="none" stroke="#888" stroke-width="1.6"><path d="M5 3l4 1 1 5-2 1c1 3 3 5 6 6l1-2 5 1 1 4c-1 2-3 2-4 2C9 20 4 15 3 7c0-1 0-3 2-4z"/></svg>
    <span class="call-sep"></span>
    <div><div class="call-label">CALL US</div><div class="call-num">555 010 2040</div></div>
  </div>
  <div class="abs btn book-btn">Book a Cleaning</div>
  <nav class="abs nav">
    <a class="active">Home</a><a>Aircraft Maintenance</a><a>Aircraft Cleaning</a><a>About Us</a><a>Contact</a><a>Careers</a>
  </nav>

  <!-- hero -->
  <section class="abs hero" role="img" aria-label="Helicopter in flight over a cloudy forested landscape">
    <div class="hero-photo"></div>
  </section>
  <svg class="abs" style="left:0;top:600px" width="1200" height="210" viewBox="0 0 1200 210">
    <path d="M0 40 C250 200 600 200 1200 15 L1200 210 L0 210 Z" fill="#fff"/>
    <path d="M0 30 C120 150 450 210 1000 80" fill="none" stroke="#1c43a8" stroke-width="7"/>
    <g transform="translate(1005 72) rotate(-30)" fill="#fff" stroke="#6a6a70" stroke-width="2">
      <path d="M-26 0 L24 0 M0 0 L-8 -22 M0 0 L-8 22 M-20 0 L-26 -9 M-20 0 L-26 9" stroke-linecap="round" stroke-width="6"/>
    </g>
  </svg>
  <h1 class="abs serif hero-title">TW AVIATION</h1>
  <p class="abs hero-text">TW Aviation is insured and all of our mechanics are licensed by the NQB with an Airframe &amp; Powerplant rating.</p>
  <div class="abs btn hero-btn">Book Now
    <svg width="16" height="16" viewBox="0 0 16 16"><circle cx="8" cy="8" r="7.5" fill="#fff"/><path d="M5 8h6M8 5l3 3-3 3" stroke="#1c43a8" stroke-width="2" fill="none"/></svg>
  </div>

  <!-- about -->
  <h2 class="abs h2 about-title">ABOUT <span>US</span></h2>
  <div class="abs about-text">
    <p>TW Aviation Services is company with aircraft maintenance experience .We focus on inspections of aircraft . Our Aircraft Mechanics who are pilots and IA's have experience many aircraft but specialize in the Kestrane KT420 , KT425 , KT435 . The Belvanko T82 and Morvell Tarrant 512 . Our focus is safety and to maintain aircraft day in and day out so our customer can operate the aircraft safely while keeping up with all the manufacturers inspections .</p>
    <p>We know aircraft maintenance &amp; maintenance planning . Leave the technical and tedious thingsto us . Get in your aircraft and fly knowing you have the best maintenance crew in the business.</p>
  </div>
  <div class="abs about-visual" role="img" aria-label="Circular illustration of a turbine fan with an aircraft climbing out of it"></div>

  <!-- what we do -->
  <svg class="abs wwd" viewBox="0 0 1200 830" preserveAspectRatio="none">
    <defs><linearGradient id="wwdBlue" x1="0" y1="0" x2="1" y2="1"><stop offset="0" stop-color="#1f46ab"/><stop offset="1" stop-color="#173c9c"/></linearGradient></defs>
    <path d="M0 175 C300 -30 850 -20 1200 190 L1200 700 C850 880 300 830 0 610 Z" fill="#6a6a70"/>
    <path d="M0 205 C300 20 850 20 1200 225 L1200 660 C850 840 300 790 0 580 Z" fill="url(#wwdBlue)"/>
  </svg>
  <h2 class="abs serif wwd-title">WHAT WE DO</h2>
  <div class="abs orbit"></div>
  <div class="abs hub-ring"></div>
  <div class="abs hub-ring2"></div>
  <div class="abs hub"><div class="brand"><span class="brand-dot" style="width:40px;height:40px"></span>TW</div></div>

  <div class="abs svc-icon" style="left:485px;top:1529px"><svg width="34" height="34" viewBox="0 0 24 24" fill="none" stroke="#fff" stroke-width="1.6"><circle cx="12" cy="12" r="4"/><path d="M12 2v4M12 18v4M2 12h4M18 12h4M5 5l3 3M16 16l3 3M5 19l3-3M16 8l3-3"/></svg></div>
  <div class="abs svc-icon" style="left:647px;top:1529px"><svg width="34" height="34" viewBox="0 0 24 24" fill="none" stroke="#fff" stroke-width="1.6"><rect x="6" y="3" width="12" height="18" rx="2"/><path d="M9 8h6M9 12h6M9 16h4"/></svg></div>
  <div class="abs svc-icon" style="left:395px;top:1629px"><svg width="34" height="34" viewBox="0 0 24 24" fill="none" stroke="#fff" stroke-width="1.6"><path d="M4 20L14 10M14 10a4 4 0 1 0 5-5l-3 3-2-2 3-3a4 4 0 0 0-5 5M4 4l16 16"/></svg></div>
  <div class="abs svc-icon" style="left:739px;top:1629px"><svg width="34" height="34" viewBox="0 0 24 24" fill="none" stroke="#fff" stroke-width="1.6"><rect x="3" y="4" width="18" height="13" rx="1"/><path d="M7 13l3-3 3 2 4-4M9 21h6"/></svg></div>
  <div class="abs svc-icon" style="left:398px;top:1757px"><svg width="34" height="34" viewBox="0 0 24 24" fill="none" stroke="#fff" stroke-width="1.6"><path d="M4 20h16M12 4v16M6 8h12M6 8l-3 6h6zM18 8l-3 6h6z"/></svg></div>
  <div class="abs svc-icon" style="left:735px;top:1757px"><svg width="34" height="34" viewBox="0 0 24 24" fill="none" stroke="#fff" stroke-width="1.6"><rect x="4" y="6" width="16" height="10" rx="1"/><circle cx="12" cy="11" r="2"/><path d="M8 20h8M12 16v4"/></svg></div>
  <div class="abs svc-icon" style="left:486px;top:1856px"><svg width="34" height="34" viewBox="0 0 24 24" fill="none" stroke="#fff" stroke-width="1.6"><rect x="4" y="3" width="12" height="6" rx="1"/><path d="M16 6h3v5h-7v3M11 14h2v7h-2z"/></svg></div>
  <div class="abs svc-icon" style="left:643px;top:1856px"><svg width="34" height="34" viewBox="0 0 24 24" fill="none" stroke="#fff" stroke-width="1.6"><circle cx="10" cy="10" r="6"/><path d="M14.5 14.5L21 21M7 10l2 2 4-4"/></svg></div>

  <div class="abs svc-label right" style="right:756px;top:1555px">Major &amp; Minor repairs</div>
  <div class="abs svc-label" style="left:767px;top:1555px">Aircraft Cleaning</div>
  <div class="abs svc-label right" style="right:848px;top:1655px">STC installations</div>
  <div class="abs svc-label" style="left:840px;top:1643px">Maintenance Tracking Utilizing<br>Tracking Programs or spreadsheets</div>
  <div class="abs svc-label right" style="right:844px;top:1783px">Aircraft Weight &amp; Balance</div>
  <div class="abs svc-label" style="left:843px;top:1772px">Removal &amp; Installation of<br>Components</div>
  <div class="abs svc-label right" style="right:755px;top:1880px">Aircraft Painting</div>
  <div class="abs svc-label" style="left:757px;top:1883px">Aircraft Pre Buy Inspections</div>

  <!-- staff -->
  <div class="abs staff-photo" role="img" aria-label="Staff member wearing a headset and cap in a helicopter cockpit"></div>
  <h2 class="abs h2 staff-title">MEET THE <span>STAFF</span></h2>
  <p class="abs staff-text">Mateus Has been an aircraft mechanic for over 10 years . He has worked for the largest sightseeing &amp; charter tourism company in the New York City area as well as repair stations &amp; manufacturers. He has aircraft specific training to the Kestrane KT420 &amp; Vornel 2K4. He has worked on several airframes including the Belvanko T82 and the Morvell 512. He has held every position in an aircraft maintenance department from mechanic up to Director of Maintenance . His work ethic and ability to manage mechanics in a organized and structured way gives any department or inspection a clear direction .</p>

  <!-- footer -->
  <svg class="abs footer-bg" viewBox="0 0 1200 465" preserveAspectRatio="none" role="img" aria-label="Faded city skyline behind the footer">
    <path d="M0 150 C300 20 700 10 1200 170 L1200 465 L0 465 Z" fill="#6a6a70"/>
    <path d="M0 150 C250 10 650 0 990 110" fill="none" stroke="#1c43a8" stroke-width="6"/>
    <g transform="translate(1005 122) rotate(-30)" stroke="#fff" stroke-linecap="round" stroke-width="6">
      <path d="M-26 0 L24 0 M0 0 L-8 -22 M0 0 L-8 22 M-20 0 L-26 -9 M-20 0 L-26 9"/>
    </g>
  </svg>
  <div class="abs brand footer-brand"><span class="brand-dot"></span>TW Aviation</div>

  <div class="abs f-head" style="left:368px;top:2760px">Our Office Address</div>
  <div class="abs f-col" style="left:368px;top:2805px">
    <div class="f-item"><svg width="12" height="12" viewBox="0 0 24 24" fill="#1c43a8"><path d="M5 3l4 1 1 5-2 1c1 3 3 5 6 6l1-2 5 1 1 4c-1 2-3 2-4 2C9 20 4 15 3 7c0-1 0-3 2-4z"/></svg><div><b>Phone</b>555 010 2040</div></div>
    <div class="f-item"><svg width="12" height="12" viewBox="0 0 24 24" fill="#1c43a8"><path d="M2 5h20v14H2z"/></svg><div><b>Email</b>info@TWAviation.example</div></div>
    <div class="f-item"><svg width="12" height="12" viewBox="0 0 24 24" fill="#1c43a8"><path d="M12 2a7 7 0 0 0-7 7c0 5 7 13 7 13s7-8 7-13a7 7 0 0 0-7-7z"/></svg><div><b>Location</b>123,Lorem ipsum dolor sit consectetur<br>adipiscing elit,</div></div>
  </div>

  <div class="abs f-head" style="left:688px;top:2760px">Company</div>
  <div class="abs f-col f-links" style="left:688px;top:2800px">Home<br>Aircraft Maintenance<br>Aircraft Cleaning<br>About Us<br>Contact<br>Careers</div>

  <div class="abs f-head" style="left:859px;top:2760px">Stil have questios?</div>
  <p class="abs f-note">Contact us using this form. A representative will aswer your questions as soon as possible.</p>
  <div class="abs btn f-btn">Get in Touch</div>

  <div class="abs go-up">&#8593; Go Up</div>
  <div class="abs f-rule"></div>
  <div class="abs f-copy">© 2020 TW Aviation | All Rights Reserved</div>
  <div class="abs f-legal"><span>Privacy Policy</span>|<span>Cookie Policy</span>|<span>Terms Of Services</span></div>
</div>
</body>
</html>
```